Business Card for a mobile physiotherapy company

I need a layout for a business card for a mobile physiotherapy company.
Slogan is "In-Home Physiotherapy - Your Path Back To Motion"
Phone number is 867-402-5913
Email VantrePhysio@mailbright.ca (subject to change with website)
Website www.VantrePhysio.ca
My name and credentials: Kent Vantre Kent Vantre, BKin, MScPT, Dry Needling
Information maybe included: Direct Billing, Services including Physiotherapy, IMS, acupuncture
Maybe include facebook and instagram logos
One side with the logo clean and sharp
Other side with details, try not to look too busy, keep everything concise

```html
<!DOCTYPE html>
<html lang="en">
<head>
<meta charset="utf-8">
<title>Vantre Physio – Business Card</title>
<link rel="stylesheet" href="https://fonts.googleapis.com/css2?family=Roboto:ital,wght@0,400;0,500;0,700;1,400&display=swap">
<style>
  :root {
    --navy: #2c4a74;
    --green: #0d5745;
    --ink: #4a4a4a;
    --paper: #ffffff;
    --backdrop: #e9e9e6;
  }
  * { box-sizing: border-box; margin: 0; padding: 0; }
  html, body {
    width: 1125px; height: 1200px; overflow: hidden;
    background: var(--backdrop);
    font-family: "Roboto", Arial, sans-serif;
  }
  .sheet { position: relative; width: 1125px; height: 1200px; }
  .card {
    position: absolute; left: 171px; width: 826px; height: 471px;
    background: var(--paper);
    box-shadow: 0 2px 6px rgba(0,0,0,0.25);
    overflow: hidden;
  }
  .card--front { top: 106px; }
  .card--back { top: 639px; }

  .identity { position: absolute; left: 59px; top: 70px; }
  .identity__name {
    font-weight: 500; font-size: 30px; color: var(--navy);
    text-transform: uppercase; line-height: 1;
  }
  .identity__credentials { font-size: 20px; color: var(--navy); margin-top: 2px; line-height: 1.15; }
  .identity__billing { font-size: 21px; font-weight: 500; color: var(--green); margin-top: 2px; line-height: 1.15; }

  .contact { position: absolute; left: 59px; top: 188px; list-style: none; }
  .contact__item {
    display: flex; align-items: center; gap: 12px;
    font-size: 20px; color: var(--ink); height: 26px;
  }
  .contact__icon { width: 18px; height: 18px; fill: var(--navy); flex: none; }

  .social { position: absolute; left: 59px; top: 282px; display: flex; gap: 4px; }
  .social__dot { width: 39px; height: 39px; border-radius: 50%; background: var(--navy); }

  .wordmark {
    font-weight: 700; color: var(--green);
    text-transform: uppercase; text-align: center; line-height: 1;
  }
  .wordmark__line { display: block; }
  .wordmark--front { position: absolute; left: 470px; width: 290px; top: 70px; }
  .wordmark--front .wordmark__main { font-size: 64px; letter-spacing: 5px; }
  .wordmark--front .wordmark__sub { font-size: 32px; letter-spacing: 15px; margin-top: 14px; margin-right: -15px; }

  .tagline-band {
    position: absolute; left: 0; bottom: 0; width: 100%; height: 105px;
    background: var(--navy); color: #fff; text-align: center;
    padding-top: 26px;
  }
  .tagline-band__slogan { font-style: italic; font-size: 19.5px; }
  .tagline-band__services { font-size: 20px; margin-top: 4px; }

  .back-mark {
    position: absolute; left: 0; width: 100%; top: 102px;
    display: flex; flex-direction: column; align-items: center;
  }
  .back-mark__dot { width: 110px; height: 110px; border-radius: 50%; background: var(--navy); }
  .wordmark--back { margin-top: 30px; }
  .wordmark--back .wordmark__main { font-size: 62px; letter-spacing: 5px; }
  .wordmark--back .wordmark__sub { font-size: 30px; letter-spacing: 15px; margin-top: 14px; margin-right: -15px; }
</style>
</head>
<body>
<main class="sheet">

  <section class="card card--front" aria-label="Card front">
    <div class="identity">
      <h1 class="identity__name">Kent Vantre</h1>
      <p class="identity__credentials">BKin, MScPT, Dry Needling</p>
      <p class="identity__billing">Direct Billing</p>
    </div>

    <ul class="contact">
      <li class="contact__item">
        <svg class="contact__icon" viewBox="0 0 24 24" aria-hidden="true"><path d="M6.6 10.8a15.1 15.1 0 0 0 6.6 6.6l2.2-2.2a1 1 0 0 1 1-.25 11.4 11.4 0 0 0 3.6.57 1 1 0 0 1 1 1V20a1 1 0 0 1-1 1A17 17 0 0 1 3 4a1 1 0 0 1 1-1h3.5a1 1 0 0 1 1 1c0 1.25.2 2.450.57 3.57a1 1 0 0 1-.25 1z"/></svg>
        867-402-5913
      </li>
      <li class="contact__item">
        <svg class="contact__icon" viewBox="0 0 24 24" aria-hidden="true"><path d="M3 5h18v14H3z M4.5 6.5v.6L12 12l7.5-4.9v-.6z" fill-rule="evenodd"/></svg>
        VantrePhysio@mailbright.ca
      </li>
      <li class="contact__item">
        <svg class="contact__icon" viewBox="0 0 24 24" aria-hidden="true"><circle cx="12" cy="12" r="10"/></svg>
        www.VantrePhysio.ca
      </li>
    </ul>

    <div class="social" aria-label="Social media">
      <span class="social__dot"></span>
      <span class="social__dot"></span>
    </div>

    <div class="wordmark wordmark--front">
      <span class="wordmark__line wordmark__main">Vantre</span>
      <span class="wordmark__line wordmark__sub">Physio</span>
    </div>

    <div class="tagline-band">
      <p class="tagline-band__slogan">In-Home Physiotherapy - Your Path Back To Motion</p>
      <p class="tagline-band__services">Physiotherapy • IMS • Acupuncture</p>
    </div>
  </section>

  <section class="card card--back" aria-label="Card back">
    <div class="back-mark">
      <span class="back-mark__dot"></span>
      <div class="wordmark wordmark--back">
        <span class="wordmark__line wordmark__main">Vantre</span>
        <span class="wordmark__line wordmark__sub">Physio</span>
      </div>
    </div>
  </section>

</main>
</body>
</html>
```